Redesign of existing business card

I would like the "signage" attachment converted into a business card. This needs to be double sided aswell, keeping the phone number and names on the front, and the email + website on the back.

Second attachment is the current business card design.

Larger font for contact details is required.

Must keep to original color themes (electric blue, silver/grey etc)

Back of the card to have blue background with white writing.

Industry/Entity Type

Business

Contact Information for Business Card

Refer to existing design from attachments

Requirements
Must have
• Refer to existing design from attachments
Nice to have

```html
<!DOCTYPE html>
<html lang="en">
<head>
<meta charset="UTF-8">
<title>Voltra Electro Services – Business Card</title>
<link rel="stylesheet" href="https://fonts.googleapis.com/css2?family=Open+Sans:wght@600;700;800&family=Orbitron:wght@500;600&display=swap">
<style>
  :root {
    --electric-blue: #0c1cf2;
    --ink-blue: #1a26e0;
    --silver: #8d8f94;
    --silver-light: #c4c6ca;
    --card-white: #ffffff;
    --backdrop: #e4e4e6;
    --text-white: #ffffff;
  }
  * { box-sizing: border-box; margin: 0; padding: 0; }
  html, body {
    width: 1200px;
    height: 900px;
    overflow: hidden;
    background: var(--backdrop);
  }
  .canvas {
    width: 1200px;
    height: 900px;
    display: flex;
    align-items: center;
    justify-content: center;
    gap: 60px;
  }
  .card {
    width: 525px;
    height: 300px;
    border-radius: 22px;
    position: relative;
    overflow: hidden;
    box-shadow: 0 6px 18px rgba(0, 0, 0, 0.14);
  }

  /* Front */
  .card-front {
    background: var(--card-white);
    font-family: "Orbitron", sans-serif;
  }
  .brand {
    position: absolute;
    left: 34px;
    top: 34px;
    display: flex;
    align-items: center;
    gap: 12px;
    font-family: "Open Sans", sans-serif;
    font-weight: 800;
    font-size: 24px;
    letter-spacing: 0.5px;
    color: var(--electric-blue);
    text-transform: uppercase;
  }
  .brand-dot {
    width: 34px;
    height: 34px;
    border-radius: 50%;
    background: var(--silver-light);
  }
  .person {
    position: absolute;
    left: 40px;
    top: 128px;
  }
  .person-name {
    font-weight: 500;
    font-size: 19px;
    letter-spacing: 1.5px;
    color: var(--silver);
    text-transform: uppercase;
  }
  .person-role {
    margin-top: 2px;
    font-weight: 500;
    font-size: 12px;
    letter-spacing: 1.5px;
    color: var(--electric-blue);
    text-transform: uppercase;
  }
  .phone {
    position: absolute;
    left: 40px;
    top: 192px;
    display: flex;
    align-items: center;
    gap: 10px;
    font-weight: 500;
    font-size: 22px;
    letter-spacing: 1px;
    color: var(--electric-blue);
  }
  .phone svg { width: 18px; height: 18px; }
  .licence {
    position: absolute;
    right: 40px;
    top: 150px;
    font-family: "Open Sans", sans-serif;
    font-weight: 700;
    font-size: 14px;
    letter-spacing: 0.5px;
    color: var(--silver);
  }

  /* Back */
  .card-back {
    background: var(--electric-blue);
    color: var(--text-white);
    font-family: "Open Sans", sans-serif;
    display: flex;
    flex-direction: column;
    justify-content: center;
    padding: 0 44px;
  }
  .tagline-main {
    font-weight: 700;
    font-size: 36px;
    line-height: 1;
    letter-spacing: 0.5px;
    text-transform: uppercase;
    text-align: center;
  }
  .tagline-sub {
    margin-top: 6px;
    font-weight: 700;
    font-size: 21px;
    letter-spacing: 0.5px;
    text-transform: uppercase;
    text-align: center;
  }
  .call-to-action {
    margin-top: 16px;
    font-weight: 700;
    font-size: 11.5px;
    letter-spacing: 0.6px;
    text-transform: uppercase;
    text-align: center;
  }
  .contact-list {
    margin-top: 14px;
    list-style: none;
    text-align: center;
    font-weight: 600;
    font-size: 21px;
    line-height: 1.25;
  }
</style>
</head>
<body>
  <main class="canvas">
    <section class="card card-front" aria-label="Business card front">
      <div class="brand">
        <span class="brand-dot"></span>
        <span class="brand-name">Voltra Electro Services</span>
      </div>
      <div class="person">
        <p class="person-name">Daniel Corwin</p>
        <p class="person-role">Director</p>
      </div>
      <p class="phone">
        <svg viewBox="0 0 24 24" aria-hidden="true"><path fill="currentColor" d="M6.6 10.8a15.1 15.1 0 0 0 6.6 6.6l2.2-2.2a1 1 0 0 1 1-.25 11.4 11.4 0 0 0 3.6.57 1 1 0 0 1 1 1V20a1 1 0 0 1-1 1A17 17 0 0 1 3 4a1 1 0 0 1 1-1h3.5a1 1 0 0 1 1 1c0 1.25.2 2.45.57 3.6a1 1 0 0 1-.25 1z"/></svg>
        0400 518 273
      </p>
      <p class="licence">EC24610</p>
    </section>

    <section class="card card-back" aria-label="Business card back">
      <h1 class="tagline-main">Your Trusted</h1>
      <h2 class="tagline-sub">Electrical Contractor</h2>
      <p class="call-to-action">Get in touch today for your free quotation</p>
      <ul class="contact-list">
        <li>daniel@voltraelectro.com</li>
        <li>www.voltraelectro.com.au</li>
      </ul>
    </section>
  </main>
</body>
</html>
```